Phone Repair Business Card

I need a business card for my mobile phone/ smart phone and tablet repair business based in New Zealand. My business name is "T.K. Repairs". I would like to see a designer make a modern phone related business card, which could incorporate something to do with the Vorlan Zeltox as this is our main repaired product. i like the dark Grey and lime green colours

```html
<!DOCTYPE html>
<html lang="en">
<head>
<meta charset="utf-8">
<title>T.K. Repairs — Business Card</title>
<link rel="stylesheet" href="https://fonts.googleapis.com/css2?family=PT+Sans&family=Oswald:wght@300&family=Bree+Serif&family=Arimo&display=swap">
<style>
  :root {
    --bg-dark: #0b0b0b;
    --bg-mid: #1e1e1e;
    --bg-glow: #3a3a3a;
    --brand-green: #1fe014;
    --slogan-grey: #a9a9a9;
    --owner-white: #ffffff;
    --detail-grey: #b3b3b3;
    --band-green: #174d10;
    --band-dark: #050505;
    --art-light: #8a9aa6;
    --art-dark: #2a3038;
  }
  html, body {
    margin: 0;
    padding: 0;
    overflow: hidden;
    background: var(--bg-dark);
  }
  .card {
    position: relative;
    width: 1200px;
    height: 686px;
    overflow: hidden;
    background:
      repeating-linear-gradient(45deg, rgba(255,255,255,0.025) 0 2px, rgba(0,0,0,0) 2px 4px),
      repeating-linear-gradient(-45deg, rgba(0,0,0,0.18) 0 2px, rgba(0,0,0,0) 2px 4px),
      radial-gradient(ellipse 560px 420px at 600px 200px, var(--bg-glow) 0%, var(--bg-mid) 55%, var(--bg-dark) 100%);
  }
  .brand-name {
    position: absolute;
    top: 36px;
    left: 0;
    width: 1252px;
    margin: 0;
    text-align: center;
    font-family: "PT Sans", sans-serif;
    font-weight: 400;
    font-size: 54px;
    letter-spacing: -1px;
    color: var(--brand-green);
  }
  .slogan {
    position: absolute;
    top: 112px;
    left: 0;
    width: 1252px;
    margin: 0;
    text-align: center;
    font-family: "Oswald", sans-serif;
    font-weight: 300;
    font-size: 29px;
    letter-spacing: 0.5px;
    color: var(--slogan-grey);
  }
  .owner {
    position: absolute;
    top: 202px;
    left: 0;
    width: 1252px;
    margin: 0;
    text-align: center;
    font-family: "Arimo", sans-serif;
    font-size: 31px;
    color: var(--owner-white);
  }
  .details {
    position: absolute;
    top: 305px;
    left: 0;
    width: 1246px;
    margin: 0;
    padding: 0;
    list-style: none;
    text-align: center;
    font-family: "Bree Serif", serif;
    font-size: 25px;
    line-height: 57px;
    color: var(--detail-grey);
  }
  .mascot-art {
    position: absolute;
    left: 914px;
    top: 258px;
    width: 270px;
    height: 398px;
    border-radius: 28px;
    background: linear-gradient(160deg, var(--art-light) 0%, var(--art-dark) 70%, rgba(0,0,0,0) 100%);
    opacity: 0.55;
  }
  .footer-band {
    position: absolute;
    left: 0;
    bottom: 0;
    width: 1200px;
    height: 19px;
    display: block;
  }
</style>
</head>
<body>
  <div class="card">
    <h1 class="brand-name">T.K. Repairs</h1>
    <p class="slogan">Comapany slogan/theme goes here</p>
    <p class="owner">Owner’s name goes here</p>
    <ul class="details">
      <li class="detail-address">Premises address goes here</li>
      <li class="detail-phone">Contact numbers goes here</li>
      <li class="detail-email">Email address goes here</li>
      <li class="detail-web">Web address goes here</li>
    </ul>
    <div class="mascot-art" role="img" aria-label="Illustration of a smartphone character waving, wearing a red stethoscope"></div>
    <svg class="footer-band" viewBox="0 0 1200 19" xmlns="http://www.w3.org/2000/svg" aria-hidden="true">
      <rect width="1200" height="19" fill="var(--band-dark)"/>
      <g fill="var(--band-green)">
        <rect x="0" y="0" width="82" height="19"/>
        <rect x="142" y="0" width="82" height="19"/>
        <rect x="288" y="0" width="82" height="19"/>
        <rect x="430" y="0" width="82" height="19"/>
        <rect x="569" y="0" width="82" height="19"/>
        <rect x="709" y="0" width="82" height="19"/>
        <rect x="853" y="0" width="82" height="19"/>
        <rect x="995" y="0" width="82" height="19"/>
        <rect x="1120" y="0" width="80" height="19"/>
      </g>
    </svg>
  </div>
</body>
</html>
```